Honey Bottle Labels for Honey Business

The honey is a niche product and the logo should exude a strong impression of wild and raw honey and natural – as in natural beekeeping. We try to keep things as simple as possible; this includes the processes the honey goes through.
We are looking for something with a gourmet / classy upmarket look and feel design. For example: Ideas with bees, honeycomb, modern or hexagonal feature; something eye catching, but not too busy.
Our honey is all natural and organic. We are a clean, simple yet sophisticated business, so would like our logo to reflect these principles.

Feel free to expand your creativity to anything you may think would look awesome and original!

The label needs to contain:
1. Our company logo. (Please see attached)
2. 100% Pure Raw Honey / Local
3. Net Wt: 16 oz (454 g) (this is the weight of the honey and will need to be modified based on bottle size.)
4. Address, Birch Hollow, MN 56999 (not larger than 1/16th inch)

Needs to be versatile to include possibility of clear label, I have included some example pictures as ideas (oval, round, square tags)

Sizes needed:
Large oval 2 5/8" x 4 1/2"
Small oval: 1 3/4" wide x 3" tall
Rectangle 1 3/4" tall x 5" wide
Round diameter 2.5"

Target Market(s)

Gourmet stores, market stall, local tourist market, potential store door sales

Requirements
Must have
• - A design that can be used on various packaging, jars and containers. We are hoping to scale up the production and want something to suit.
• - has to have a wow to stand out on the supermarket shelves
Nice to have
• Things we like:
• Minimalist designs
• Clever designs
• We don't like hand drawn font types
• We are open to the use of a hexagon in the logo, but not must have
Should not have
• Things we do not like:
• Too many colors

```html
<!DOCTYPE html>
<html lang="en">
<head>
<meta charset="utf-8">
<title>Meadowlark Honey – Oval Jar Label</title>
<link rel="stylesheet" href="https://fonts.googleapis.com/css2?family=Montserrat:wght@700&family=Quicksand:wght@500&display=swap">
<style>
  :root {
    --canvas-bg: #f4f4f2;
    --label-white: #ffffff;
    --honey-light: #fbbd2c;
    --honey-deep: #f39a12;
    --honey-ink: #f5a21a;
    --text-dark: #2e2111;
    --comb-edge: #5a3a12;
    --comb-light: #ffe07a;
    --comb-mid: #f7b733;
  }
  html, body {
    margin: 0;
    padding: 0;
    width: 1200px;
    height: 1200px;
    overflow: hidden;
    background: var(--canvas-bg);
  }
  .label-canvas {
    position: relative;
    width: 1200px;
    height: 1200px;
  }
  .label-art {
    display: block;
    width: 1200px;
    height: 1200px;
  }
  .arc-text {
    font-family: "Montserrat", sans-serif;
    font-weight: 700;
    font-size: 34px;
    letter-spacing: 3px;
    fill: var(--text-dark);
  }
  .brand-name {
    font-family: "Quicksand", sans-serif;
    font-weight: 500;
    fill: var(--honey-ink);
  }
</style>
</head>
<body>
<main class="label-canvas">
  <svg class="label-art" viewBox="0 0 1200 1200" xmlns="http://www.w3.org/2000/svg">
    <defs>
      <linearGradient id="honey-fill" x1="0" y1="0" x2="0" y2="1">
        <stop offset="0" stop-color="var(--honey-deep)"/>
        <stop offset="0.5" stop-color="var(--honey-light)"/>
        <stop offset="1" stop-color="var(--honey-deep)"/>
      </linearGradient>
      <linearGradient id="comb-fill" x1="0" y1="0" x2="0" y2="1">
        <stop offset="0" stop-color="var(--comb-light)"/>
        <stop offset="1" stop-color="var(--comb-mid)"/>
      </linearGradient>
      <path id="arc-top" d="M 400 620 A 200 395 0 0 1 800 620"/>
      <path id="arc-bottom" d="M 375 620 A 225 420 0 0 0 825 620"/>
    </defs>

    <!-- seal strip -->
    <rect class="seal-strip" x="535" y="20" width="130" height="200" fill="var(--label-white)"/>

    <!-- oval label body -->
    <ellipse class="label-border" cx="600" cy="620" rx="272" ry="468" fill="var(--label-white)"/>
    <ellipse class="label-field" cx="600" cy="620" rx="250" ry="446" fill="url(#honey-fill)"/>

    <!-- honeycomb ribbon -->
    <rect class="comb-ribbon" x="547" y="176" width="106" height="290"
          fill="url(#comb-fill)" stroke="var(--comb-edge)" stroke-width="6"
          role="img" aria-label="Honeycomb ribbon with a daisy and green leaves at its base"/>

    <!-- curved wording -->
    <text class="arc-text"><textPath href="#arc-top" startOffset="9%">100% PURE</textPath></text>
    <text class="arc-text"><textPath href="#arc-top" startOffset="60%">RAW HONEY</textPath></text>
    <text class="arc-text" text-anchor="middle"><textPath href="#arc-bottom" startOffset="50%">BIRCH HOLLOW, MN 56999</textPath></text>

    <!-- side dashed rules -->
    <path class="side-rule" d="M 408 447 A 212 410 0 0 0 408 793" fill="none" stroke="var(--text-dark)" stroke-width="2" stroke-dasharray="7 6"/>
    <path class="side-rule" d="M 792 447 A 212 410 0 0 1 792 793" fill="none" stroke="var(--text-dark)" stroke-width="2" stroke-dasharray="7 6"/>
    <polygon class="side-hex" points="388,606 400,613 400,627 388,634 376,627 376,613" fill="var(--comb-edge)"/>
    <polygon class="side-hex" points="812,606 824,613 824,627 812,634 800,627 800,613" fill="var(--comb-edge)"/>

    <!-- brand medallion -->
    <circle class="medallion" cx="600" cy="655" r="188" fill="var(--label-white)"/>
    <circle class="medallion-ring" cx="600" cy="655" r="174" fill="none" stroke="var(--honey-ink)" stroke-width="4"/>
    <circle class="brand-dot" cx="600" cy="600" r="14" fill="var(--honey-ink)"/>
    <text class="brand-name" x="600" y="690" text-anchor="middle" font-size="46">meadowlark</text>
    <text class="brand-name" x="600" y="740" text-anchor="middle" font-size="46">honey</text>
  </svg>
</main>
</body>
</html>
```